A clean crisp business card for a Landscape Construction company. Designed to be easy to read contact/ info and also be appealing/interesting, unlike a traditional business card.

Industry/Entity Type

Landscape Construction

Contact Information for Business Card

Company name : Bramblecrest Landscape Construction, phone number: (877) 62Vales, website:Bramblecrestlandscapes.example, Email, sales@bramblecrestlandscapes.example

Requirements
Nice to have
• Luxurious finishes/ details…. Icons or emblems next to contact info
Should not have
• Clipart or general pictures

```html
<!DOCTYPE html>
<html lang="en">
<head>
<meta charset="utf-8">
<title>Bramblecrest Landscape Construction — Business Card</title>
<link rel="stylesheet" href="https://fonts.googleapis.com/css2?family=Cinzel:wght@500;600&family=Libre+Baskerville:wght@400;700&display=swap">
<style>
  :root {
    --canvas-bg: #d9dadc;
    --brand-blue: #1a6aae;
    --brand-blue-deep: #155a96;
    --brand-green: #8cc63f;
    --card-white: #f4f4f4;
    --ink: #111111;
    --ink-soft: #222222;
    --white: #ffffff;
  }
  * { box-sizing: border-box; margin: 0; padding: 0; }
  html, body {
    width: 1200px;
    height: 800px;
    overflow: hidden;
    background: var(--canvas-bg);
  }
  .canvas {
    position: relative;
    width: 1200px;
    height: 800px;
  }
  .card {
    position: absolute;
    width: 520px;
    height: 297px;
    overflow: hidden;
    box-shadow: 0 10px 28px rgba(0,0,0,0.22);
  }
  .card-frame {
    position: absolute;
    inset: 0;
    width: 100%;
    height: 100%;
  }

  /* Front */
  .card-front {
    left: 130px;
    top: 90px;
    background: var(--brand-blue);
  }
  .front-mark {
    position: absolute;
    left: 0;
    right: 0;
    top: 96px;
    display: flex;
    flex-direction: column;
    align-items: center;
    color: var(--white);
    font-family: "Cinzel", serif;
    font-weight: 600;
    text-align: center;
  }
  .front-mark .mark-dot {
    width: 38px;
    height: 38px;
    border-radius: 50%;
    background: var(--white);
    margin-bottom: 12px;
  }
  .front-mark .mark-name {
    font-size: 34px;
    letter-spacing: 1px;
    line-height: 1;
  }
  .front-mark .mark-sub {
    font-size: 11px;
    letter-spacing: 3.4px;
    margin-top: 6px;
  }

  /* Back */
  .card-back {
    left: 550px;
    top: 410px;
    background: var(--card-white);
  }
  .back-mark {
    position: absolute;
    left: 46px;
    top: 40px;
    display: flex;
    align-items: center;
    gap: 10px;
    color: var(--brand-blue);
    font-family: "Cinzel", serif;
    font-weight: 600;
  }
  .back-mark .mark-dot {
    width: 26px;
    height: 26px;
    border-radius: 50%;
    background: var(--brand-blue);
  }
  .back-mark .mark-text {
    display: flex;
    flex-direction: column;
    line-height: 1;
  }
  .back-mark .mark-name { font-size: 22px; }
  .back-mark .mark-sub { font-size: 7.5px; letter-spacing: 2px; margin-top: 3px; }

  .company-name {
    position: absolute;
    left: 46px;
    top: 112px;
    font-family: "Libre Baskerville", serif;
    font-weight: 700;
    font-size: 15px;
    line-height: 1.3;
    color: var(--ink);
    text-transform: uppercase;
  }
  .contact-list {
    position: absolute;
    left: 46px;
    top: 172px;
    list-style: none;
    display: flex;
    flex-direction: column;
    gap: 9px;
  }
  .contact-item {
    display: flex;
    align-items: center;
    gap: 10px;
    font-family: "Libre Baskerville", serif;
    font-size: 12.5px;
    color: var(--ink-soft);
  }
  .contact-icon {
    width: 22px;
    height: 22px;
    flex: none;
  }
</style>
</head>
<body>
<main class="canvas">

  <section class="card card-front" aria-label="Business card front">
    <svg class="card-frame" viewBox="0 0 520 297" aria-hidden="true">
      <defs>
        <linearGradient id="front-frame-stroke" x1="0" y1="1" x2="1" y2="0">
          <stop offset="0" stop-color="#9acd3c"/>
          <stop offset="0.45" stop-color="#8cc63f"/>
          <stop offset="1" stop-color="#1a6aae" stop-opacity="0.2"/>
        </linearGradient>
      </defs>
      <rect x="28" y="32" width="492" height="234" fill="none" stroke="url(#front-frame-stroke)" stroke-width="2.2"/>
    </svg>
    <div class="front-mark">
      <span class="mark-dot"></span>
      <span class="mark-name">Bramblecrest</span>
      <span class="mark-sub">LANDSCAPE CONSTRUCTION</span>
    </div>
  </section>

  <section class="card card-back" aria-label="Business card back">
    <svg class="card-frame" viewBox="0 0 520 297" aria-hidden="true">
      <defs>
        <linearGradient id="back-frame-stroke" x1="1" y1="0" x2="0" y2="0">
          <stop offset="0" stop-color="#1a6aae"/>
          <stop offset="0.5" stop-color="#1a6aae" stop-opacity="0.75"/>
          <stop offset="1" stop-color="#1a6aae" stop-opacity="0"/>
        </linearGradient>
      </defs>
      <rect x="-2" y="26" width="490" height="246" fill="none" stroke="url(#back-frame-stroke)" stroke-width="2.4"/>
    </svg>

    <div class="back-mark">
      <span class="mark-dot"></span>
      <span class="mark-text">
        <span class="mark-name">Bramblecrest</span>
        <span class="mark-sub">LANDSCAPE CONSTRUCTION</span>
      </span>
    </div>

    <h1 class="company-name">Bramblecrest<br>Landscape Construction</h1>

    <ul class="contact-list">
      <li class="contact-item">
        <svg class="contact-icon" viewBox="0 0 22 22" aria-hidden="true">
          <circle cx="11" cy="11" r="11" fill="var(--brand-blue)"/>
          <path d="M7.2 6.2c.5-.4 1.1-.3 1.4.2l1 1.6c.3.5.2 1-.2 1.3l-.6.5c.5 1.2 1.4 2.1 2.6 2.6l.5-.6c.3-.4.9-.5 1.3-.2l1.6 1c.5.3.6.9.2 1.4l-.7.8c-.5.6-1.4.8-2.2.4-2.5-1.1-4.4-3-5.5-5.5-.4-.8-.2-1.7.4-2.2z" fill="#fff"/>
        </svg>
        <span>(877) 62Vales</span>
      </li>
      <li class="contact-item">
        <svg class="contact-icon" viewBox="0 0 22 22" aria-hidden="true">
          <circle cx="11" cy="11" r="11" fill="var(--brand-blue)"/>
          <g fill="none" stroke="#fff" stroke-width="1">
            <circle cx="11" cy="11" r="5.5"/>
            <ellipse cx="11" cy="11" rx="2.4" ry="5.5"/>
            <path d="M5.5 11h11M6.3 8.2h9.4M6.3 13.8h9.4"/>
          </g>
        </svg>
        <span>Bramblecrestlandscapes.example</span>
      </li>
      <li class="contact-item">
        <svg class="contact-icon" viewBox="0 0 22 22" aria-hidden="true">
          <circle cx="11" cy="11" r="11" fill="var(--brand-blue)"/>
          <g fill="none" stroke="#fff" stroke-width="1.1" stroke-linejoin="round">
            <rect x="5.5" y="7.3" width="11" height="7.6"/>
            <path d="M5.5 7.3l5.5 4.4 5.5-4.4"/>
          </g>
        </svg>
        <span>sales@bramblecrestlandscapes.example</span>
      </li>
    </ul>
  </section>

</main>
</body>
</html>
```